My contest is to create a front and back cover for my new book. It is a Kids Drawing Pad that will be 8 x 10. I will want the files in ai, pdf, png, & jpg.
My idea is a black background with big letters that say "Drawing Pad for Kids". Very little to none illustrations, we can try a few and see how it looks. I am thinking almost block letters colored in different colors.

```html
<!DOCTYPE html>
<html lang="en">
<head>
<meta charset="UTF-8">
<title>Drawing Pad for Kids – Cover</title>
<link rel="stylesheet" href="https://fonts.googleapis.com/css2?family=Cabin+Sketch:wght@700&display=swap">
<style>
  :root {
    --page-bg: #ededed;
    --frame-dark: #1f1f1f;
    --frame-mid: #2b2b2b;
    --panel-black: #000000;
    --chalk-white: #f4f4f4;
    --chalk-red: #e3201b;
    --chalk-blue: #2aa3dc;
    --chalk-green: #25b34a;
  }

  html, body {
    margin: 0;
    padding: 0;
    width: 1200px;
    height: 1200px;
    overflow: hidden;
    background: var(--page-bg);
  }

  .canvas {
    position: relative;
    width: 1200px;
    height: 1200px;
    display: flex;
    align-items: center;
    justify-content: center;
  }

  .cover {
    position: relative;
    width: 800px;
    height: 1000px;
    box-shadow: 0 6px 18px rgba(0, 0, 0, 0.25);
  }

  .cover-pattern {
    position: absolute;
    inset: 0;
    background: linear-gradient(135deg, var(--frame-mid) 0%, var(--frame-dark) 100%);
  }

  .title-panel {
    position: absolute;
    top: 105px;
    left: 85px;
    right: 100px;
    bottom: 145px;
    background: var(--panel-black);
    display: flex;
    flex-direction: column;
    align-items: center;
    justify-content: center;
    gap: 14px;
  }

  .title {
    margin: 0;
    font-family: "Cabin Sketch", cursive;
    font-weight: 700;
    text-transform: uppercase;
    text-align: center;
    line-height: 1;
    display: flex;
    flex-direction: column;
    align-items: center;
    gap: 22px;
  }

  .title-line { display: block; letter-spacing: 2px; }
  .title-drawing { color: var(--chalk-white); font-size: 96px; }
  .title-pad     { color: var(--chalk-red);   font-size: 104px; }
  .title-for     { color: var(--chalk-blue);  font-size: 74px; }
  .title-kids    { color: var(--chalk-green); font-size: 90px; }
</style>
</head>
<body>
  <main class="canvas">
    <section class="cover">
      <div class="cover-pattern" role="img" aria-label="Border pattern of small colourful birdhouses, sprigs and dots in red, green, blue and yellow on charcoal"></div>
      <div class="title-panel">
        <h1 class="title">
          <span class="title-line title-drawing">Drawing</span>
          <span class="title-line title-pad">Pad</span>
          <span class="title-line title-for">For</span>
          <span class="title-line title-kids">Kids!</span>
        </h1>
      </div>
    </section>
  </main>
</body>
</html>
```